Business cards & stationery for a mortgage brokerage
Pebblewick Mortgages
Modern
Owen Drisdale
Director
17-19 Marsh Lane
Fernby Hollow
LT4 7QW
owen@pebblewickmortgages.co.uk
www.pebblewickmortgages.co.uk
Is it also possible to have this in an editable format? We will be using the design for a number of employees so we need to change some personal details
use your initiative on this please, but we would like it bright and colourful

```html
<!DOCTYPE html>
<html lang="en">
<head>
<meta charset="utf-8">
<title>Pebblewick Mortgages – Business Card</title>
<link rel="stylesheet" href="https://fonts.googleapis.com/css2?family=Questrial&family=Open+Sans:wght@400;600&display=swap">
<style>
  :root {
    --page-bg: #e9ecea;
    --green-dark: #1f6b22;
    --green: #2e8b2e;
    --green-mid: #3f9e2f;
    --lime: #a8c728;
    --lime-light: #d3e27a;
    --white: #ffffff;
    --ink-on-green: #eaf5e4;
    --shadow: rgba(20, 40, 20, 0.22);
  }
  * { box-sizing: border-box; margin: 0; padding: 0; }
  html, body {
    width: 1200px; height: 1009px; overflow: hidden;
    background: var(--page-bg);
  }
  .sheet {
    width: 1200px; height: 1009px;
    display: flex; flex-direction: column; align-items: center; justify-content: center;
    gap: 34px;
  }
  .card {
    position: relative;
    width: 720px; height: 452px;
    border-radius: 26px;
    overflow: hidden;
    box-shadow: 0 12px 30px var(--shadow);
  }
  .card-art { position: absolute; inset: 0; width: 100%; height: 100%; }

  /* Front */
  .brand {
    position: absolute; left: 70px; top: 78px;
    display: flex; align-items: center; gap: 16px;
  }
  .brand-dot {
    width: 52px; height: 52px; border-radius: 50%;
    background: var(--lime);
  }
  .brand-name {
    font-family: "Questrial", sans-serif;
    font-size: 42px; color: var(--green);
    letter-spacing: -0.5px; line-height: 1;
  }
  .tagline {
    position: absolute; left: 140px; top: 134px;
    font-family: "Open Sans", sans-serif; font-weight: 600;
    font-size: 13px; letter-spacing: 3.6px; color: var(--green-mid);
    text-transform: uppercase;
  }
  .person {
    position: absolute; left: 110px; top: 318px;
    font-family: "Open Sans", sans-serif; color: var(--white);
  }
  .person-name { font-size: 19px; font-weight: 600; }
  .person-role { font-size: 14px; margin-top: 4px; color: var(--ink-on-green); }

  .contact {
    position: absolute; left: 388px; top: 262px;
    font-family: "Open Sans", sans-serif; font-size: 13.5px;
    color: var(--white); line-height: 1.55;
    list-style: none;
  }
  .contact li { display: flex; align-items: center; gap: 10px; }
  .contact .address { padding-left: 24px; }
  .contact .address + .address { margin-bottom: 6px; }
  .contact svg { width: 14px; height: 14px; flex: none; fill: var(--white); }

  /* Back */
  .back-brand {
    position: absolute; right: 48px; bottom: 86px;
    font-family: "Questrial", sans-serif;
    font-size: 50px; color: var(--white); line-height: 1;
  }
  .back-tagline {
    position: absolute; right: 50px; bottom: 58px;
    font-family: "Open Sans", sans-serif; font-weight: 600;
    font-size: 14px; letter-spacing: 4px; color: var(--lime-light);
    text-transform: uppercase;
  }
</style>
</head>
<body>
<main class="sheet">

  <section class="card card-front" aria-label="Business card front">
    <svg class="card-art" viewBox="0 0 720 452" preserveAspectRatio="none" aria-hidden="true">
      <defs>
        <linearGradient id="frontGreen" x1="0" y1="0" x2="1" y2="1">
          <stop offset="0" stop-color="#3c9a2c"/>
          <stop offset="1" stop-color="#1f6b22"/>
        </linearGradient>
      </defs>
      <rect width="720" height="452" fill="#ffffff"/>
      <path d="M0 228 C180 300 420 160 720 196 L720 452 L0 452 Z" fill="#a8c728"/>
      <path d="M0 244 C190 312 430 182 720 214 L720 452 L0 452 Z" fill="url(#frontGreen)"/>
    </svg>

    <div class="brand">
      <span class="brand-dot"></span>
      <span class="brand-name">Pebblewick Mortgages</span>
    </div>
    <p class="tagline">Clear advice, steady homes</p>

    <div class="person">
      <p class="person-name">Owen Drisdale</p>
      <p class="person-role">Director</p>
    </div>

    <ul class="contact">
      <li class="address">17-19 Marsh Lane</li>
      <li class="address">Fernby Hollow, LT4 7QW</li>
      <li>
        <svg viewBox="0 0 24 24"><path d="M6.6 10.8a15 15 0 0 0 6.6 6.6l2.2-2.2a1 1 0 0 1 1-.25 11.4 11.4 0 0 0 3.6.57 1 1 0 0 1 1 1V20a1 1 0 0 1-1 1A17 17 0 0 1 3 4a1 1 0 0 1 1-1h3.5a1 1 0 0 1 1 1c0 1.25.2 2.45.57 3.6a1 1 0 0 1-.25 1z"/></svg>
        01632 960044
      </li>
      <li>
        <svg viewBox="0 0 24 24"><path d="M7 1h10a2 2 0 0 1 2 2v18a2 2 0 0 1-2 2H7a2 2 0 0 1-2-2V3a2 2 0 0 1 2-2zm0 3v14h10V4zm5 15.5a1 1 0 1 0 0 2 1 1 0 0 0 0-2z"/></svg>
        07700 900398
      </li>
      <li>
        <svg viewBox="0 0 24 24"><path d="M2 5h20v14H2zm2 2v.5l8 5 8-5V7zm0 2.8V17h16V9.8l-8 5z"/></svg>
        owen@pebblewickmortgages.co.uk
      </li>
      <li>
        <svg viewBox="0 0 24 24"><path d="M12 2a10 10 0 1 0 0 20 10 10 0 0 0 0-20zm6.9 9h-3a15 15 0 0 0-1.3-5.6A8 8 0 0 1 18.9 11zM12 4.1c.9 1.2 1.8 3.6 1.9 6.9h-3.8c.1-3.3 1-5.7 1.9-6.9zM9.4 5.4A15 15 0 0 0 8.1 11h-3a8 8 0 0 1 4.3-5.6zM5.1 13h3a15 15 0 0 0 1.3 5.6A8 8 0 0 1 5.1 13zm6.9 6.9c-.9-1.200-1.8-3.6-1.9-6.9h3.8c-.1 3.3-1 5.7-1.9 6.9zm2.6-1.3a15 15 0 0 0 1.3-5.6h3a8 8 0 0 1-4.3 5.6z"/></svg>
        www.pebblewickmortgages.co.uk
      </li>
    </ul>
  </section>

  <section class="card card-back" aria-label="Business card back">
    <svg class="card-art" viewBox="0 0 720 452" preserveAspectRatio="none" aria-hidden="true">
      <defs>
        <linearGradient id="backGreen" x1="0" y1="0" x2="1" y2="1">
          <stop offset="0" stop-color="#3f9e2f"/>
          <stop offset="1" stop-color="#1f6b22"/>
        </linearGradient>
      </defs>
      <rect width="720" height="452" fill="url(#backGreen)"/>
    </svg>
    <p class="back-brand">Pebblewick Mortgages</p>
    <p class="back-tagline">Clear advice, steady homes</p>
  </section>

</main>
</body>
</html>
```